جمعية سنابل لصحة المرأة
جمعية سنابل لصحة المرأة Tamsara Women's health society
جمعية سنابل لصحة المرأة - Health
Creative Brief
Simple
Tamsara Women's health society
Riyadh Saudi Arabia
tamsara.whs@nelvomail.com
http://www.tamsara-example.org/
if also can have design on Mugs tshirts pins pens shopping bag thank you
same information but in arabic

```html
<!DOCTYPE html>
<html lang="en">
<head>
<meta charset="utf-8">
<title>Tamsara Women's Health Society – Business Card</title>
<link href="https://fonts.googleapis.com/css2?family=Montserrat:wght@400;500;600;700&family=Cairo:wght@500;700&display=swap" rel="stylesheet">
<style>
  :root {
    --bg: #e9e8ec;
    --card: #ffffff;
    --purple: #7a4e9c;
    --purple-soft: #9c7bb8;
    --lavender: #dccfe8;
    --lavender-light: #eee6f4;
    --ink: #444048;
    --muted: #6f6a74;
  }
  * { margin: 0; padding: 0; box-sizing: border-box; }
  html, body { width: 1200px; height: 751px; overflow: hidden; }
  body {
    background: var(--bg);
    font-family: "Montserrat", sans-serif;
    color: var(--ink);
    position: relative;
  }
  .card {
    position: absolute;
    top: 216px;
    width: 492px;
    height: 283px;
    background: var(--card);
    border-radius: 14px;
    overflow: hidden;
    box-shadow: 0 2px 8px rgba(0,0,0,0.12);
  }
  .card--front { left: 91px; }
  .card--back { left: 619px; }

  .decor { position: absolute; top: 0; height: 100%; }
  .card--front .decor { right: 0; width: 190px; }
  .card--back .decor { left: 0; width: 115px; }

  .brand {
    position: absolute;
    left: 29px;
    top: 31px;
    display: flex;
    align-items: center;
    gap: 12px;
  }
  .brand__dot {
    width: 44px; height: 44px;
    border-radius: 50%;
    background: var(--purple);
  }
  .brand__text { display: flex; flex-direction: column; line-height: 1; }
  .brand__arabic {
    font-family: "Cairo", sans-serif;
    font-weight: 700;
    font-size: 18px;
    color: var(--purple);
    direction: rtl;
    text-align: left;
  }
  .brand__name {
    font-weight: 700;
    font-size: 20px;
    color: var(--purple);
    letter-spacing: 0.5px;
    margin-top: 2px;
  }
  .brand__tag {
    font-size: 6.5px;
    font-weight: 500;
    color: var(--purple-soft);
    letter-spacing: 0.6px;
    margin-top: 3px;
  }
  .brand__tag-ar {
    font-family: "Cairo", sans-serif;
    font-size: 8px;
    color: var(--purple-soft);
    direction: rtl;
    text-align: left;
    margin-top: 2px;
  }

  .person { position: absolute; left: 29px; top: 136px; }
  .person__name { font-size: 12.5px; font-weight: 700; color: var(--purple); }
  .person__role { font-size: 9.5px; color: var(--muted); margin-top: 4px; }

  .contact { position: absolute; left: 29px; top: 192px; font-size: 9px; color: var(--ink); }
  .contact__city { margin-bottom: 11px; }
  .contact__row { display: flex; align-items: center; gap: 8px; margin-bottom: 7px; }
  .contact__row svg { width: 11px; height: 11px; }

  .back-brand {
    position: absolute;
    left: 270px;
    right: 0;
    top: 122px;
    text-align: center;
    line-height: 1;
  }
  .back-brand__arabic {
    font-family: "Cairo", sans-serif;
    font-weight: 700;
    font-size: 30px;
    color: var(--purple);
    direction: rtl;
  }
  .back-brand__name {
    font-weight: 700;
    font-size: 30px;
    color: var(--purple);
    letter-spacing: 1px;
    margin-top: 2px;
  }
  .back-brand__tag {
    font-size: 8px;
    font-weight: 500;
    color: var(--purple-soft);
    letter-spacing: 1px;
    margin-top: 4px;
  }
  .back-brand__tag-ar {
    font-family: "Cairo", sans-serif;
    font-size: 12px;
    font-weight: 500;
    color: var(--purple);
    direction: rtl;
    margin-top: 6px;
  }
  .back-brand__url {
    font-size: 12px;
    font-weight: 600;
    color: var(--purple);
    margin-top: 8px;
    letter-spacing: 0.3px;
  }
</style>
</head>
<body>

  <section class="card card--front">
    <svg class="decor" viewBox="0 0 190 283" preserveAspectRatio="none" role="img" aria-label="Large faint lavender decorative motif area">
      <defs>
        <radialGradient id="decorFront" cx="0.6" cy="0.45" r="0.7">
          <stop offset="0" stop-color="#dccfe8"/>
          <stop offset="1" stop-color="#eee6f4"/>
        </radialGradient>
      </defs>
      <rect width="190" height="283" fill="url(#decorFront)"/>
    </svg>

    <div class="brand">
      <div class="brand__dot"></div>
      <div class="brand__text">
        <span class="brand__arabic">سنابل</span>
        <span class="brand__name">TAMSARA</span>
        <span class="brand__tag">WOMEN HEALTH SOCIETY</span>
        <span class="brand__tag-ar">جمعية سنابل لصحة المرأة</span>
      </div>
    </div>

    <div class="person">
      <p class="person__name">Noura Haddad</p>
      <p class="person__role">Founder</p>
    </div>

    <div class="contact">
      <p class="contact__city">Qasrah, Al Noor Region</p>
      <p class="contact__row">
        <svg viewBox="0 0 12 12" aria-hidden="true"><circle cx="6" cy="6" r="6" fill="var(--purple)"/><rect x="3" y="4" width="6" height="4" fill="none" stroke="#fff" stroke-width="0.8"/><path d="M3 4 L6 6.3 L9 4" fill="none" stroke="#fff" stroke-width="0.8"/></svg>
        tamsara.whs@nelvomail.com
      </p>
      <p class="contact__row">
        <svg viewBox="0 0 12 12" aria-hidden="true"><circle cx="6" cy="6" r="6" fill="var(--purple)"/><circle cx="6" cy="6" r="3" fill="none" stroke="#fff" stroke-width="0.8"/><path d="M3 6 H9 M6 3 V9" stroke="#fff" stroke-width="0.6"/></svg>
        www.tamsara-example.org
      </p>
    </div>
  </section>

  <section class="card card--back">
    <svg class="decor" viewBox="0 0 115 283" preserveAspectRatio="none" role="img" aria-label="Large faint lavender decorative motif area">
      <defs>
        <radialGradient id="decorBack" cx="0.4" cy="0.45" r="0.7">
          <stop offset="0" stop-color="#dccfe8"/>
          <stop offset="1" stop-color="#eee6f4"/>
        </radialGradient>
      </defs>
      <rect width="115" height="283" fill="url(#decorBack)"/>
    </svg>

    <div class="back-brand">
      <p class="back-brand__arabic">سنابل</p>
      <p class="back-brand__name">TAMSARA</p>
      <p class="back-brand__tag">WOMEN HEALTH SOCIETY</p>
      <p class="back-brand__tag-ar">جمعية سنابل لصحة المرأة</p>
      <p class="back-brand__url">www.tamsara-example.org</p>
    </div>
  </section>

</body>
</html>
```